Plumwave business card

We need a modern business card - With our 4 colors - See web: www.plumwave.dk

I have attached logo and som old business Cards we have - Lets Make the new ones shine...:-) -

Industry/Entity Type

Business

Requirements
Must have
• the logo with plumwave only,

```html
<!DOCTYPE html>
<html lang="da">
<head>
<meta charset="utf-8">
<title>Plumwave visitkort</title>
<link href="https://fonts.googleapis.com/css2?family=Source+Sans+3:wght@400;600;700&display=swap" rel="stylesheet">
<style>
  :root {
    --stage: #000000;
    --paper: #ffffff;
    --orange: #f3861f;
    --green: #8dc63f;
    --ink: #3a3a3a;
    --ink-soft: #2b2b2b;
  }
  * { margin: 0; padding: 0; box-sizing: border-box; }
  html, body {
    width: 1200px;
    height: 900px;
    overflow: hidden;
    background: var(--stage);
    font-family: "Source Sans 3", "Myriad Pro", Arial, sans-serif;
  }
  .canvas { position: relative; width: 1200px; height: 900px; }

  .card { position: absolute; top: 200px; width: 310px; height: 502px; }
  .card--front {
    left: 265px;
    background: var(--paper);
    border-radius: 62px 0 62px 0;
  }
  .card--back {
    left: 641px;
    width: 309px;
    background: var(--orange);
    border-radius: 0 62px 0 62px;
  }

  /* front: brand block */
  .brand {
    position: absolute;
    left: 73px;
    top: 112px;
    width: 181px;
    text-align: center;
  }
  .brand__name {
    display: flex;
    align-items: center;
    justify-content: center;
    gap: 8px;
    font-size: 25px;
    font-weight: 400;
    letter-spacing: 1.5px;
    color: var(--ink-soft);
    line-height: 1;
  }
  .brand__dot {
    width: 12px; height: 12px;
    border-radius: 50%;
    background: var(--green);
  }
  .brand__rule {
    margin-top: 38px;
    height: 2px;
    background: var(--green);
  }
  .brand__tagline {
    margin-top: 9px;
    font-size: 11px;
    color: var(--ink-soft);
  }

  /* front: person */
  .person { position: absolute; left: 27px; top: 327px; }
  .person__name {
    font-size: 18px;
    font-weight: 600;
    color: var(--green);
    text-transform: uppercase;
    letter-spacing: 0.2px;
  }
  .person__role { margin-top: 2px; font-size: 13.5px; color: var(--ink); }

  .contact { list-style: none; margin-top: 26px; }
  .contact__item {
    display: flex;
    align-items: center;
    gap: 6px;
    font-size: 13.5px;
    color: var(--ink);
    line-height: 19px;
  }
  .contact__icon { width: 11px; height: 11px; flex: none; }

  /* back */
  .back__mark {
    position: absolute;
    left: 0; right: 0;
    top: 200px;
    text-align: center;
    font-size: 40px;
    font-weight: 400;
    letter-spacing: 2px;
    color: var(--paper);
  }
  .back__address {
    position: absolute;
    left: 0; right: 0;
    top: 368px;
    text-align: center;
    font-size: 17.5px;
    font-weight: 700;
    line-height: 22px;
    color: var(--paper);
    text-transform: uppercase;
  }
</style>
</head>
<body>
<main class="canvas">
  <section class="card card--front">
    <div class="brand">
      <div class="brand__name"><span class="brand__dot"></span>plumwave</div>
      <div class="brand__rule"></div>
      <p class="brand__tagline">Medier til unge</p>
    </div>

    <div class="person">
      <h1 class="person__name">Sigrid Halvorsen</h1>
      <p class="person__role">Salgsdirektør</p>
      <ul class="contact">
        <li class="contact__item">
          <svg class="contact__icon" viewBox="0 0 12 12" aria-hidden="true"><path fill="#8dc63f" d="M1 4.5C1 3 3 2 6 2s5 1 5 2.5V6H8.5V4.8h-5V6H1zM3 6.5h6l1.5 3.5h-9z"/></svg>
          +45 61 42 73 18
        </li>
        <li class="contact__item">
          <svg class="contact__icon" viewBox="0 0 12 12" aria-hidden="true"><rect x="1" y="2.5" width="10" height="7" fill="#8dc63f"/><path d="M1.5 3l4.5 3.5L10.5 3" fill="none" stroke="#fff" stroke-width="1"/></svg>
          sh@plumwave.dk
        </li>
        <li class="contact__item">
          <svg class="contact__icon" viewBox="0 0 12 12" aria-hidden="true"><g fill="none" stroke="#8dc63f" stroke-width="1.5" stroke-linecap="round"><path d="M5 7L7 5"/><path d="M6.5 3.5l1-1a2 2 0 0 1 2.8 2.8l-1 1"/><path d="M5.5 8.5l-1 1a2 2 0 0 1-2.8-2.8l1-1"/></g></svg>
          www.plumwave.dk
        </li>
      </ul>
    </div>
  </section>

  <section class="card card--back">
    <div class="back__mark">plumwave</div>
    <p class="back__address">Lindevangs Allé 14 - 2000<br>Frederiksberg -Tlf. 32 47 19 60</p>
  </section>
</main>
</body>
</html>
```